Amber Ridge Publishing Web Page Design

Design a website for my new start up publishing company - Amber Ridge Publishing, the first work published by ARP with be a new book by M.R. Theodor called Silent Ledger. The prototype for the book cover is attached.

Target Market(s)

Worldwide, all readers of mystery, fiction, etc.

Industry/Entity Type

Book Publisher

Coding

Coded - Design and coding required

Number of Pages Required

1 page

```html
<!DOCTYPE html>
<html lang="en">
<head>
<meta charset="utf-8">
<title>Amber Ridge Publishing — Silent Ledger</title>
<link rel="stylesheet" href="https://fonts.googleapis.com/css2?family=Libre+Baskerville:ital,wght@0,400;0,700;1,400&family=Open+Sans:wght@400;600;700&display=swap">
<style>
:root{
  --cream:#f3f1ea;
  --white:#ffffff;
  --ink:#1d1d1f;
  --muted:#8a8a8a;
  --navy:#1f2a5a;
  --accent-blue:#2b3d9a;
  --gold:#c99a4a;
  --band:#3d3d3d;
  --line:#cfcfcf;
  --soft-blue:#a9cbe6;
  --serif:'Libre Baskerville', Georgia, serif;
  --sans:'Open Sans', Arial, sans-serif;
}
*{box-sizing:border-box;margin:0;padding:0}
html,body{width:1200px;height:4615px;overflow:hidden}
body{position:relative;background:var(--cream);font-family:var(--sans);color:var(--ink)}
.btn{position:absolute;display:flex;align-items:center;justify-content:center;font-family:var(--sans);font-size:12px;font-weight:700;letter-spacing:1px;text-transform:uppercase;border:1px solid var(--navy);color:var(--ink);background:var(--white)}
.btn--dark{background:var(--navy);color:var(--white)}
.btn--round{border-radius:18px;border-color:#fff;background:rgba(255,255,255,.25)}
.section-title{position:absolute;left:0;width:1200px;text-align:center;font-family:var(--serif);font-weight:700;font-size:44px;color:var(--ink)}
.body-text{font-size:14px;line-height:1.75;color:var(--muted)}

/* hero */
.hero{position:absolute;left:0;top:0;width:1200px;height:558px}
.hero__bg{position:absolute;inset:0;background:linear-gradient(100deg,#dcdcd8 0%,#eceae5 35%,#f4f3ef 60%,#e3e6e6 100%)}
.hero__veil{position:absolute;inset:0;background:rgba(255,255,255,.35)}
.brand{position:absolute;left:30px;top:46px;font-family:var(--serif);font-weight:700;font-size:18px;letter-spacing:1px;color:var(--ink);text-transform:uppercase}
.menu-icon{position:absolute;right:34px;top:48px}
.hero__cover{position:absolute;left:338px;top:135px;width:189px;height:403px;background:linear-gradient(160deg,#1b2a6b,#0c1640 60%,#2b3a8a);box-shadow:12px 10px 18px rgba(0,0,0,.35)}
.hero__title{position:absolute;left:642px;top:176px;font-family:var(--serif);font-size:38px;font-weight:400;color:var(--ink)}
.hero__by{position:absolute;left:644px;top:226px;font-family:var(--serif);font-style:italic;font-size:14px;color:var(--muted)}
.hero__text{position:absolute;left:644px;top:266px;width:400px;font-size:13px;line-height:1.7;color:#555}

/* categories */
.tile{position:absolute;transform:rotate(-12deg);box-shadow:4px 6px 12px rgba(0,0,0,.25);z-index:1}
.tile--front{z-index:3}
.tile__img{position:absolute;inset:0}
.tile__label{position:absolute;background:var(--white);padding:7px 14px;font-size:12px;color:var(--ink);white-space:nowrap;box-shadow:0 2px 6px rgba(0,0,0,.2)}

/* about */
.about__backdrop{position:absolute;left:204px;top:1722px;width:282px;height:340px;background:var(--soft-blue)}
.about__photo{position:absolute;left:231px;top:1680px;width:282px;height:358px;background:linear-gradient(180deg,#d9dde0,#b8bcc0 60%,#9aa0a6)}
.about__title{position:absolute;left:608px;top:1660px;font-family:var(--serif);font-weight:700;font-size:40px}
.about__text{position:absolute;left:610px;top:1740px;width:470px}
.about__sign{position:absolute;left:610px;top:1872px;width:120px;height:40px;background:linear-gradient(90deg,#c9c9c9,#e6e4df)}
.about__name{position:absolute;left:610px;top:1958px;font-family:var(--serif);font-weight:700;font-size:16px;letter-spacing:1px}
.about__role{position:absolute;left:610px;top:1994px;font-size:12px;color:var(--muted)}

/* intro */
.intro{position:absolute;left:0;top:2135px;width:1200px;height:520px;background:var(--white)}
.intro__kicker{position:absolute;left:173px;top:2250px;font-size:13px;letter-spacing:5px;color:var(--accent-blue);text-transform:uppercase}
.intro__title{position:absolute;left:173px;top:2286px;font-family:var(--serif);font-weight:400;font-size:46px}
.intro__text{position:absolute;left:173px;top:2360px;width:400px}
.intro__old{position:absolute;left:173px;top:2480px;font-family:var(--serif);font-weight:700;font-size:26px;color:#b5b5b5;text-decoration:line-through}
.intro__new{position:absolute;left:290px;top:2480px;font-family:var(--serif);font-weight:700;font-size:26px;color:var(--gold)}
.intro__cover{position:absolute;left:673px;top:2223px;width:181px;height:354px;background:linear-gradient(160deg,#1b2a6b,#0c1640 60%,#2b3a8a);box-shadow:12px 10px 18px rgba(0,0,0,.3)}

/* sample */
.sample__sub{position:absolute;left:0;width:1200px;top:2776px;text-align:center;font-family:var(--serif);font-style:italic;font-size:34px;color:var(--accent-blue)}
.sample__cover{position:absolute;left:173px;top:2854px;width:346px;height:484px;background:linear-gradient(160deg,#1b2a6b,#0c1640 60%,#2b3a8a);box-shadow:16px 14px 24px rgba(0,0,0,.35)}
.chapter{position:absolute;left:538px;width:493px;height:46px;border-bottom:1px solid var(--line);display:flex;align-items:center;justify-content:space-between;font-size:13px;font-weight:700;letter-spacing:1px}
.chapter__icon{width:22px;height:22px;border:1px solid #777;border-radius:50%;display:flex;align-items:center;justify-content:center;font-weight:400;font-size:15px;color:#555}
.chapter__body{position:absolute;left:538px;top:2942px;width:470px;font-size:13px;line-height:1.75;color:var(--muted)}

/* you might like */
.like{position:absolute;left:0;top:3346px;width:1200px;height:827px;background:var(--white)}
.book{position:absolute;top:3604px;width:146px;text-align:center}
.book__cover{width:146px;height:223px;box-shadow:4px 6px 10px rgba(0,0,0,.25)}
.book__price{margin-top:14px;font-size:12px;color:var(--gold);font-weight:600}
.book__title{margin-top:8px;font-family:var(--serif);font-size:14px}
.book__author{margin-top:4px;font-size:11px;color:var(--muted)}

/* share band */
.band{position:absolute;left:0;top:4173px;width:1200px;height:192px;background:var(--band)}
.band__title{position:absolute;left:173px;top:4226px;font-family:var(--serif);font-weight:700;font-size:28px;color:var(--white)}
.band__text{position:absolute;left:173px;top:4272px;font-size:12px;color:#bdbdbd}
.social{position:absolute;top:4240px;width:32px;height:32px;border:1px solid #bdbdbd;border-radius:50%}
.band__cover{position:absolute;left:892px;top:4146px;width:62px;height:181px;background:linear-gradient(160deg,#1b2a6b,#0c1640 60%,#2b3a8a);box-shadow:6px 6px 12px rgba(0,0,0,.4)}

/* footer */
.footer{position:absolute;left:0;top:4365px;width:1200px;height:250px;background:var(--white)}
.footer__title{position:absolute;left:0;width:1200px;top:4412px;text-align:center;font-family:var(--serif);font-weight:400;font-size:54px}
.footer__by{position:absolute;left:0;width:1200px;top:4488px;text-align:center;font-size:13px;color:var(--muted);letter-spacing:1px}
.footer__copy{position:absolute;left:0;width:1200px;top:4588px;text-align:center;font-size:11px;color:var(--muted)}
</style>
</head>
<body>

<header class="hero">
  <div class="hero__bg" role="img" aria-label="Photo of a bright living room with a reader relaxing by the window"></div>
  <div class="hero__veil"></div>
  <div class="brand">Amber Ridge Publishing</div>
  <svg class="menu-icon" width="20" height="16" viewBox="0 0 20 16"><rect y="0" width="20" height="2.5" fill="#1d1d1f"/><rect y="6.5" width="20" height="2.5" fill="#1d1d1f"/><rect y="13" width="20" height="2.5" fill="#1d1d1f"/></svg>
  <div class="hero__cover" role="img" aria-label="Silent Ledger book cover"></div>
  <h1 class="hero__title">Silent Ledger</h1>
  <div class="hero__by">by M.R. Theodor</div>
  <p class="hero__text">Follow a quiet ledger clerk as hidden debts surface, old alliances crack, and one missing page threatens to unravel a careful town.</p>
  <div class="btn btn--round" style="left:654px;top:454px;width:211px;height:36px">Buy Now</div>
</header>

<h2 class="section-title" style="top:712px">Category of Books</h2>

<div class="tile" style="left:0;top:935px;width:120px;height:160px"><div class="tile__img" role="img" aria-label="Fantasy books photo" style="background:linear-gradient(150deg,#cfd3d6,#8e969c)"></div><div class="tile__label" style="left:14px;top:60px">Fantasy</div></div>
<div class="tile tile--front" style="left:185px;top:985px;width:190px;height:215px"><div class="tile__img" role="img" aria-label="Crime thriller books photo" style="background:linear-gradient(150deg,#4a4038,#1e1a17)"></div><div class="tile__label" style="left:58px;top:90px">Crime Thriller</div></div>
<div class="tile" style="left:415px;top:870px;width:205px;height:170px"><div class="tile__img" role="img" aria-label="Science fiction books photo" style="background:linear-gradient(150deg,#7b8186,#2f3438)"></div><div class="tile__label" style="left:60px;top:70px">Science Fiction</div></div>
<div class="tile" style="left:745px;top:862px;width:190px;height:215px"><div class="tile__img" role="img" aria-label="Romance books photo" style="background:linear-gradient(150deg,#c8a88e,#6d5548)"></div><div class="tile__label" style="left:78px;top:100px">Romance</div></div>
<div class="tile" style="left:968px;top:825px;width:215px;height:235px"><div class="tile__img" role="img" aria-label="Adventure books photo" style="background:linear-gradient(150deg,#b9b3a6,#6e6658)"></div><div class="tile__label" style="left:105px;top:92px">Adventure</div></div>
<div class="tile" style="left:30px;top:1135px;width:250px;height:195px"><div class="tile__img" role="img" aria-label="Children's books illustration" style="background:linear-gradient(150deg,#9cc08a,#d6735a)"></div><div class="tile__label" style="left:36px;top:112px">Children's Books</div></div>
<div class="tile" style="left:330px;top:1150px;width:215px;height:255px"><div class="tile__img" role="img" aria-label="Fiction books photo" style="background:linear-gradient(150deg,#8f969b,#4b5257)"></div><div class="tile__label" style="left:80px;top:120px">Fiction</div></div>
<div class="tile" style="left:610px;top:1055px;width:245px;height:255px"><div class="tile__img" role="img" aria-label="Recipe books photo of a plated dish" style="background:linear-gradient(150deg,#d9cfc0,#c0503a)"></div><div class="tile__label" style="left:110px;top:120px">Recipe</div></div>
<div class="tile" style="left:898px;top:1130px;width:245px;height:275px"><div class="tile__img" role="img" aria-label="Philosophy books photo of a statue" style="background:linear-gradient(150deg,#b7c4cf,#8c8d8a)"></div><div class="tile__label" style="left:80px;top:140px">Philosophy</div></div>

<div class="btn" style="left:538px;top:1522px;width:124px;height:32px;font-size:11px">View More</div>

<div class="about__backdrop" role="img" aria-label="Light blue decorative panel behind the author portrait"></div>
<div class="about__photo" role="img" aria-label="Portrait photo of the author"></div>
<h2 class="about__title">About The Author</h2>
<p class="about__text body-text">M.R. Theodor writes mysteries shaped by quiet towns, careful records and the secrets people keep. After years working in archives, the author turned to fiction, building tense stories around overlooked details. Silent Ledger is the first novel from a writer who believes every page can hide a clue.</p>
<div class="about__sign" role="img" aria-label="Author's handwritten signature"></div>
<div class="about__name">M.R. THEODOR</div>
<div class="about__role">Author</div>

<section class="intro"></section>
<div class="intro__kicker">Introducing</div>
<h2 class="intro__title">Silent Ledger</h2>
<p class="intro__text body-text">A gripping debut mystery about numbers that do not add up, a town that would rather forget, and a clerk who cannot stop asking questions.</p>
<div class="intro__old">$28.00</div>
<div class="intro__new">$23.00</div>
<div class="btn btn--dark" style="left:173px;top:2554px;width:135px;height:31px;font-size:10px">Quick View</div>
<div class="btn" style="left:327px;top:2554px;width:142px;height:31px;font-size:10px">Add to Cart</div>
<div class="intro__cover" role="img" aria-label="Silent Ledger book cover"></div>

<h2 class="section-title" style="top:2724px;font-size:36px">Experience First Pages</h2>
<div class="sample__sub">For Free</div>
<div class="sample__cover" role="img" aria-label="Silent Ledger book cover"></div>
<div class="chapter" style="top:2882px"><span>CHAPTER 01</span><span class="chapter__icon">&minus;</span></div>
<p class="chapter__body">The rain had not stopped for three days when Ada found the ledger tucked behind the counter. Its pages were neat, its totals exact, yet one column had been quietly erased. She closed the book and locked the door.</p>
<div class="chapter" style="top:3066px"><span>CHAPTER 02</span><span class="chapter__icon">+</span></div>
<div class="chapter" style="top:3132px"><span>CHAPTER 03</span><span class="chapter__icon">+</span></div>
<div class="btn btn--dark" style="left:538px;top:3231px;width:147px;height:31px;font-size:10px">Reviews</div>
<div class="btn" style="left:715px;top:3231px;width:162px;height:31px;font-size:10px">View Book</div>

<section class="like"></section>
<h2 class="section-title" style="top:3444px;font-size:40px">You Might Like</h2>
<div class="book" style="left:77px"><div class="book__cover" role="img" aria-label="Book cover with a wildcat illustration" style="background:linear-gradient(160deg,#8a6a2a,#2b3a1c)"></div><div class="book__price">$18.00</div><div class="book__title">Harbor Lights</div><div class="book__author">By Lena Marsh</div></div>
<div class="book" style="left:254px"><div class="book__cover" role="img" aria-label="Book cover with a dark green scene" style="background:linear-gradient(160deg,#3b4a2c,#14180f)"></div><div class="book__price">$18.00</div><div class="book__title">Winter Field</div><div class="book__author">By Owen Hale</div></div>
<div class="book" style="left:431px"><div class="book__cover" role="img" aria-label="Book cover with a red emblem" style="background:linear-gradient(160deg,#e8e2d8,#b2241f)"></div><div class="book__price">$18.00</div><div class="book__title">Red Signal</div><div class="book__author">By Tara Voss</div></div>
<div class="book" style="left:604px"><div class="book__cover" role="img" aria-label="Book cover in bright green" style="background:linear-gradient(160deg,#b7d83a,#6f8f14)"></div><div class="book__price">$18.00</div><div class="book__title">Empty Rooms</div><div class="book__author">By Paul Greer</div></div>
<div class="book" style="left:781px"><div class="book__cover" role="img" aria-label="Book cover with a night city" style="background:linear-gradient(160deg,#2a4a6a,#0d1b2a)"></div><div class="book__price">$18.00</div><div class="book__title">Glass Waltz</div><div class="book__author">By Ida Krane</div></div>
<div class="book" style="left:958px"><div class="book__cover" role="img" aria-label="Book cover in blue and yellow" style="background:linear-gradient(160deg,#2e5f9e,#e3c33a)"></div><div class="book__price">$18.00</div><div class="book__title">Small Crimes</div><div class="book__author">By Nina Ford</div></div>
<div class="btn" style="left:538px;top:3970px;width:124px;height:32px;font-size:11px">View More</div>

<section class="band"></section>
<div class="band__title">Like This Book?</div>
<div class="band__text">Share now!</div>
<div class="social" style="left:465px"></div>
<div class="social" style="left:523px"></div>
<div class="social" style="left:581px"></div>
<div class="social" style="left:639px"></div>
<div class="band__cover" role="img" aria-label="Silent Ledger book cover"></div>

<footer class="footer"></footer>
<h2 class="footer__title">Silent Ledger</h2>
<div class="footer__by">By M.R. THEODOR</div>
<div class="btn btn--dark" style="left:442px;top:4530px;width:146px;height:30px;font-size:10px">Add to Cart</div>
<div class="btn" style="left:615px;top:4530px;width:147px;height:30px;font-size:10px">View Book</div>
<div class="footer__copy">All rights reserved | Amber Ridge Publishing</div>

</body>
</html>
```